A hand soap seller needs a premium label for a new product

We need a premium label for a bottle of soap. We want to write on it:
VANTROSELLA (Name)
Hypoallergenic and antibacterial hand soap
350 ml e / 11.8 fl oz (volume, http://pimaxo.ru/7K3RtWbqmeL519)
Saint Petersburg - Russia / www.vantrosella.ru
We want to see the face of a hippopotamus in the design. Use only black and white and green for accents (the color of grass). Examples of a hippopotamus are shown in the photo. Our soap is hypoallergenic. Ideal for both children and adults. Therefore, the label should appeal to adults and children.
The bottle will be white, and the soap dispenser will be black.
So I'm attaching an example of a soap design that we liked
Label size: height-78 mm, width-102 mm !!!

Target Market(s)

Mothers and children

Industry/Entity Type

Hand soap

Font styles to use
Serif

Colors

Designer to choose only greyscale colors for use in the design.

Requirements
Must have
• The face of a hippopotamus emerging from the grass, Black and white palette with elements of green (grass color)
Nice to have
• The face of a hippopotamus emerging from the grass
Should not have
• Different colors

```html
<!DOCTYPE html>
<html lang="en">
<head>
<meta charset="utf-8">
<title>VANTROSELLA Hand Soap Label</title>
<link rel="stylesheet" href="https://fonts.googleapis.com/css2?family=Advent+Pro:wght@300;400;500&display=swap">
<style>
  :root {
    --label-black: #0b0b0b;
    --label-charcoal: #1c1c1c;
    --grass-deep: #1f6a32;
    --grass-mid: #3f8f3a;
    --grass-light: #72a23f;
    --brand-green: #45a845;
    --ink-white: #ffffff;
    --mascot-grey: #aebdc6;
    --mascot-shadow: #6f7478;
  }
  * { margin: 0; padding: 0; box-sizing: border-box; }
  html, body {
    width: 1200px; height: 918px; overflow: hidden;
    background: var(--label-black);
  }
  .label {
    position: relative;
    width: 1200px; height: 918px;
    overflow: hidden;
    background:
      radial-gradient(ellipse 900px 700px at 75% 30%, #1e1e1e 0%, transparent 70%),
      radial-gradient(ellipse 700px 500px at 20% 90%, #161616 0%, transparent 70%),
      var(--label-black);
    font-family: "Advent Pro", sans-serif;
    color: var(--ink-white);
  }
  .swoosh { position: absolute; inset: 0; width: 1200px; height: 918px; }
  .brand-line {
    position: absolute; left: 145px; top: 88px;
    font-size: 108px; font-weight: 400; line-height: 1;
    color: var(--brand-green); letter-spacing: 1px;
  }
  .brand-rule {
    position: absolute; left: 146px; top: 196px;
    width: 364px; height: 4px; background: var(--brand-green);
  }
  .product-name {
    position: absolute; left: 146px; top: 222px;
    font-size: 66px; font-weight: 500; line-height: 1;
    letter-spacing: 0;
  }
  .product-type {
    position: absolute; left: 140px; top: 286px;
    font-size: 146px; font-weight: 400; line-height: 1;
    letter-spacing: 1px;
  }
  .mascot {
    position: absolute; left: 136px; top: 485px;
    width: 377px; height: 408px;
  }
  .details {
    position: absolute; right: 62px; top: 700px;
    text-align: right; font-weight: 400;
  }
  .volume {
    font-size: 52px; line-height: 1;
    padding-bottom: 8px;
    border-bottom: 4px solid var(--ink-white);
  }
  .origin { font-size: 36px; line-height: 1.15; margin-top: 10px; }
  .website { font-size: 36px; line-height: 1.15; }
</style>
</head>
<body>
<main class="label">
  <svg class="swoosh" viewBox="0 0 1200 918" aria-hidden="true">
    <path d="M0,758 C300,790 520,760 710,620 C900,480 1060,300 1200,0 L1200,190 C1060,390 900,560 660,700 C460,812 250,862 0,872 Z" fill="var(--grass-deep)"/>
    <path d="M0,738 C260,762 480,742 660,660 C860,560 1060,350 1200,120 L1200,290 C1010,520 810,640 610,720 C410,792 210,830 0,850 Z" fill="var(--grass-mid)" opacity="0.75"/>
    <path d="M0,730 C260,752 470,735 640,660 C840,570 1050,360 1200,110 L1200,160 C1050,380 850,580 650,675 C470,752 260,772 0,762 Z" fill="var(--grass-light)" opacity="0.85"/>
    <path d="M0,880 C280,862 520,790 760,640 C960,510 1100,360 1200,210" fill="none" stroke="#0a0a0a" stroke-width="3"/>
  </svg>

  <div class="brand-line">verdalis</div>
  <div class="brand-rule"></div>
  <div class="product-name">VANTROSELLA</div>
  <div class="product-type">Hand Soap</div>

  <svg class="mascot" viewBox="0 0 377 408" role="img" aria-label="Cartoon hippopotamus mascot sitting on a soft grey shadow">
    <defs>
      <radialGradient id="mascotFill" cx="50%" cy="45%" r="60%">
        <stop offset="0%" stop-color="#c9d5dc"/>
        <stop offset="100%" stop-color="var(--mascot-grey)"/>
      </radialGradient>
    </defs>
    <ellipse cx="185" cy="365" rx="182" ry="36" fill="var(--mascot-shadow)" opacity="0.85"/>
    <path d="M120,20 C200,0 300,30 320,90 C340,150 300,190 280,220 C320,280 330,340 300,380 L70,380 C40,330 50,260 90,210 C90,150 70,60 120,20 Z" fill="url(#mascotFill)"/>
  </svg>

  <div class="details">
    <div class="volume">350 ml e / 11,8 fl.oz.</div>
    <div class="origin">saints-petersburg - russia</div>
    <div class="website">www.vantrosella.ru</div>
  </div>
</main>
</body>
</html>
```